Business card for psychiatrist

Business card design project for a psychiatristWe would like to have the impression of 1. We (patient and the doctor) are working together.2. Light the way so that patients can see where they are going and what their goals are.3. One side of the business card will have the letter "TFP" which stands for Thornvale Family Psychiatry.4. The other side of the business card will have the address, phone number, name of the psychiatrist, website, etc.5. A logo could go into either side of the business card. Let's see what looks better.
Business card design project for a psychiatrist
We would like to have the impression of
1. We (patient and the doctor) are working together.
2. Light the way so that patients can see where they are going and what their goals are.
3. One side of the business card will have the letter "TFP" which stands for Thornvale Family Psychiatry.
4. The other side of the business card will have the address, phone number, name of the psychiatrist, website, etc.
5. A logo could go into either side of the business card. Let's see what looks better.
Colors
Designer to choose colors to be used in the design.
Look and feel
Each slider illustrates characteristics of the customer's brand and the style your logo design should communicate.

```html
<!DOCTYPE html>
<html lang="en">
<head>
<meta charset="utf-8">
<title>Thornvale Family Psychiatry – Business Card</title>
<link href="https://fonts.googleapis.com/css2?family=Source+Sans+3:wght@400;600&display=swap" rel="stylesheet">
<style>
  :root {
    --backdrop: #3b3b3c;
    --card: #ffffff;
    --brand-blue: #0f4c81;
    --brand-green: #4a8a3c;
    --text-grey: #6e6e70;
    --rule-grey: #7a7a7c;
  }
  * { margin: 0; padding: 0; box-sizing: border-box; }
  html, body {
    width: 1200px; height: 999px; overflow: hidden;
    background: var(--backdrop);
    font-family: "Source Sans 3", "Myriad Pro", Arial, sans-serif;
  }
  .canvas { position: relative; width: 1200px; height: 999px; }

  .card {
    position: absolute; width: 794px; height: 453px;
    background: var(--card); border-radius: 30px; overflow: hidden;
  }
  .card--front { left: 133px; top: 44px; }
  .card--back  { left: 193px; top: 518px; }

  /* brand lockup: plain name with one circle */
  .brand { position: absolute; display: flex; align-items: center; gap: 22px; color: var(--brand-blue); }
  .brand__dot { border-radius: 50%; background: var(--brand-blue); flex: none; }
  .brand__name { font-weight: 400; line-height: 1; }
  .brand__name span { display: block; }
  .brand__main { letter-spacing: 0.5px; }
  .brand__sub { letter-spacing: 2px; margin-top: 8px; }

  .card--front .brand { left: 200px; top: 74px; }
  .card--front .brand__dot { width: 64px; height: 64px; }
  .card--front .brand__main { font-size: 54px; }
  .card--front .brand__sub { font-size: 21px; }

  .card--back .brand { left: 150px; top: 175px; }
  .card--back .brand__dot { width: 80px; height: 80px; }
  .card--back .brand__main { font-size: 66px; }
  .card--back .brand__sub { font-size: 25px; margin-top: 10px; }

  .person { position: absolute; left: 0; right: 0; top: 230px; text-align: center; }
  .person__name { font-size: 32px; color: var(--brand-blue); line-height: 1; letter-spacing: -0.3px; }
  .person__role { font-size: 17px; color: var(--text-grey); margin-top: 10px; }

  .address { position: absolute; left: 0; right: 0; top: 328px; text-align: center; font-size: 16px; color: var(--text-grey); }
  .rule { position: absolute; left: 0; right: 0; top: 361px; height: 3px; background: var(--rule-grey); }

  .contacts { position: absolute; top: 372px; font-size: 17px; color: var(--text-grey); list-style: none; }
  .contacts--left { left: 58px; }
  .contacts--right { left: 463px; }
  .contacts li { display: flex; align-items: center; gap: 18px; height: 29px; }
  .contacts svg { width: 20px; height: 20px; fill: var(--brand-blue); flex: none; }
</style>
</head>
<body>
<main class="canvas">

  <section class="card card--front" aria-label="Business card, contact side">
    <div class="brand">
      <div class="brand__dot"></div>
      <div class="brand__name"><span class="brand__main">THORNVALE</span><span class="brand__sub">FAMILY PSYCHIATRY</span></div>
    </div>

    <div class="person">
      <p class="person__name">Name Title</p>
      <p class="person__role">designation</p>
    </div>

    <p class="address">suit # 00, Lorem ipsum Lorem Lorem ipsum</p>
    <div class="rule"></div>

    <ul class="contacts contacts--left">
      <li>
        <svg viewBox="0 0 20 20" aria-hidden="true"><rect x="1" y="1" width="18" height="18" rx="3"/><path d="M7 4c-1 1-1.5 2.5-.5 5s3 5 4.5 6c1 .6 2 .4 2.8-.3l-2-2.2-1.3.8c-1-.6-2.3-2.4-2.7-3.6l1.2-.9L8 4z" fill="#fff"/></svg>
        000-000-0000
      </li>
      <li>
        <svg viewBox="0 0 20 20" aria-hidden="true"><rect x="5" y="1" width="10" height="7"/><rect x="1" y="8" width="18" height="11" rx="2"/><rect x="5" y="11" width="10" height="2" fill="#fff"/><rect x="5" y="14.5" width="10" height="2" fill="#fff"/></svg>
        000-000-0000
      </li>
    </ul>

    <ul class="contacts contacts--right">
      <li>
        <svg viewBox="0 0 20 20" aria-hidden="true"><path d="M1 8l9-6 9 6v11H1z"/><path d="M3 9l7 5 7-5" fill="none" stroke="#fff" stroke-width="1.6"/></svg>
        abcd@abcdefgh.com
      </li>
      <li>
        <svg viewBox="0 0 20 20" aria-hidden="true"><rect x="6" y="1" width="3" height="10" rx="1.5"/><path d="M6 9h9a2 2 0 0 1 2 2v4c0 2.5-2 4-4 4H9c-2 0-3-1-4-2.5L3 12c-.4-1 .8-1.8 1.6-1L6 12z"/></svg>
        www.abcdefgh.com
      </li>
    </ul>
  </section>

  <section class="card card--back" aria-label="Business card, brand side">
    <div class="brand">
      <div class="brand__dot"></div>
      <div class="brand__name"><span class="brand__main">THORNVALE</span><span class="brand__sub">FAMILY PSYCHIATRY</span></div>
    </div>
  </section>

</main>
</body>
</html>
```